Business Card for Wellness Clinic

We need a business card for our new logo. I want it to match the feel of the logo

Target Market(s)

Young professional families looking for holistic health care

Industry/Entity Type

Health And Wellness

Contact Information for Business Card

Our business Name: Brackenfield Health & wellness Centre, our phone #, email address...see attached old business card

Font styles to use
Sans Serif

Colors
33b8a4
cee9f5

Requirements
Must have
• my logo and business name
• Font is "Helvetica Neue LT Std 45 Light" and
• Only for "&" using font "Trajan pro bold"
• Use colors in the logo

```html
<!DOCTYPE html>
<html lang="en">
<head>
<meta charset="utf-8">
<title>Brackenfield Health &amp; Wellness Centre – Business Card</title>
<link href="https://fonts.googleapis.com/css2?family=Roboto:wght@300;400&display=swap" rel="stylesheet">
<style>
  :root {
    --teal: #33b8a4;
    --ink: #3a3a3a;
    --muted: #8a8a8a;
    --card: #ffffff;
    --backdrop: #2b2b2b;
  }
  * { box-sizing: border-box; margin: 0; padding: 0; }
  html, body { width: 1200px; height: 873px; overflow: hidden; }
  body {
    background: var(--backdrop);
    font-family: "Roboto", "Helvetica Neue", Arial, sans-serif;
    font-weight: 300;
    color: var(--ink);
    display: flex;
    flex-direction: column;
    align-items: center;
    justify-content: center;
    gap: 40px;
  }
  .card {
    position: relative;
    width: 640px;
    height: 366px;
    background: var(--card);
    border-radius: 18px;
  }

  /* shared */
  .tag {
    position: absolute;
    background: var(--teal);
    color: #fff;
    font-size: 17px;
    letter-spacing: 1px;
    text-transform: uppercase;
    padding: 3px 10px;
  }
  .brand {
    position: absolute;
    display: flex;
    align-items: center;
    gap: 12px;
  }
  .brand-mark { width: 38px; height: 38px; background: var(--teal); flex: none; }
  .brand-name {
    color: var(--teal);
    font-weight: 300;
    text-transform: uppercase;
    letter-spacing: 3px;
    line-height: 1.35;
  }

  /* appointment side */
  .appt-tag { left: 200px; top: 34px; }
  .field { position: absolute; font-size: 16px; color: var(--muted); display: flex; align-items: flex-end; gap: 6px; }
  .field .dots { border-bottom: 2px dotted #b5b5b5; height: 14px; }
  .date { left: 40px; top: 96px; }
  .date .dots { width: 200px; }
  .time { left: 300px; top: 96px; }
  .time .dots { width: 110px; }
  .ampm { position: absolute; left: 480px; top: 94px; display: flex; gap: 18px; }
  .days { position: absolute; left: 40px; right: 30px; top: 150px; display: flex; justify-content: space-between; }
  .check { display: flex; align-items: center; gap: 4px; font-size: 15px; color: var(--muted); }
  .check .box { width: 20px; height: 18px; border: 2px solid var(--teal); border-radius: 3px; }
  .days .check:first-child { color: var(--ink); }
  .policy-tag { left: 40px; top: 206px; }
  .policy-text { position: absolute; left: 40px; top: 242px; width: 340px; font-size: 15px; line-height: 1.4; color: var(--ink); }
  .appt-brand { left: 400px; top: 250px; }
  .appt-brand .brand-name { font-size: 13px; }

  /* contact side */
  .front-brand { left: 40px; top: 48px; }
  .front-brand .brand-name { font-size: 17px; }
  .person { position: absolute; right: 40px; top: 140px; text-align: right; }
  .person-name { color: var(--teal); font-size: 22px; font-weight: 400; }
  .person-role { font-size: 15px; font-weight: 400; color: #222; margin-top: 2px; }
  .rule { position: absolute; height: 3px; background: var(--teal); }
  .rule-upper { right: 40px; width: 300px; top: 196px; }
  .rule-lower { left: 40px; width: 300px; top: 236px; }
  .contacts { position: absolute; left: 40px; top: 256px; list-style: none; }
  .contacts li { display: flex; align-items: center; gap: 12px; font-size: 17px; margin-bottom: 9px; color: #333; }
  .contacts svg { width: 18px; height: 18px; flex: none; }
</style>
</head>
<body>

  <section class="card card-appointment" aria-label="Appointment card">
    <span class="tag appt-tag">Next Appointment</span>

    <div class="field date">Date: <span class="dots"></span></div>
    <div class="field time">Time: <span class="dots"></span></div>
    <div class="ampm">
      <span class="check">AM <span class="box"></span></span>
      <span class="check">PM <span class="box"></span></span>
    </div>

    <div class="days">
      <span class="check">Mon <span class="box"></span></span>
      <span class="check">Tue <span class="box"></span></span>
      <span class="check">Wed <span class="box"></span></span>
      <span class="check">Thu <span class="box"></span></span>
      <span class="check">Fri <span class="box"></span></span>
      <span class="check">Sat <span class="box"></span></span>
      <span class="check">Sun <span class="box"></span></span>
    </div>

    <span class="tag policy-tag">Cancellation Policy</span>
    <p class="policy-text">If you are unable to keep your appointment, pl provide atleast 2 business daysnotice or full visit fee will apply.</p>

    <div class="brand appt-brand">
      <span class="brand-mark"></span>
      <span class="brand-name">Brackenfield Health<br>&amp; Wellness Centre</span>
    </div>
  </section>

  <section class="card card-contact" aria-label="Contact card">
    <div class="brand front-brand">
      <span class="brand-mark"></span>
      <span class="brand-name">Brackenfield Health<br>&amp; Wellness Centre</span>
    </div>

    <div class="person">
      <p class="person-name">Dr. Maren Holt, N.D</p>
      <p class="person-role">Naturopathic Doctor</p>
    </div>
    <span class="rule rule-upper"></span>
    <span class="rule rule-lower"></span>

    <ul class="contacts">
      <li>
        <svg viewBox="0 0 18 18" aria-hidden="true"><rect x="4" y="1" width="10" height="16" rx="2" fill="none" stroke="var(--teal)" stroke-width="2"/></svg>
        613-555-0142
      </li>
      <li>
        <svg viewBox="0 0 18 18" aria-hidden="true"><rect x="1" y="3" width="16" height="12" fill="var(--teal)"/><path d="M1 3 L9 10 L17 3" fill="none" stroke="#fff" stroke-width="1.5"/></svg>
        mholt@brackenfieldnaturopathic.ca
      </li>
      <li>
        <svg viewBox="0 0 18 18" aria-hidden="true"><path d="M9 1 C5 1 3 4 3 7 C3 11 9 17 9 17 C9 17 15 11 15 7 C15 4 13 1 9 1 Z" fill="var(--teal)"/><circle cx="9" cy="7" r="2.3" fill="#fff"/></svg>
        48 Alder Row, Suite 12, Ottawa, ON K1R 7T2
      </li>
    </ul>
  </section>

</body>
</html>
```